Velmo BUSINESS CARD

Design an attention-grabbing business cards. Draw inspiration from the provided logo file. Please use the same font style as in the logo.
the back side of the card is for accent/decoration.

Contact Information for Business Card

PLEASE USE PROVIDED BUSINESS CARD SAMPLE

Other font styles liked:
• LUMETTE

Colors
EB3D1F
EC4F4E
F09395
F8D3D4
FCEDEE

Requirements
Must have
• RED, BLACK COLORS, SOLID BACK COLOR
Nice to have
• MAKE IT FANCY

```html
<!DOCTYPE html>
<html lang="en">
<head>
<meta charset="utf-8">
<title>Velmo Business Card</title>
<link rel="stylesheet" href="https://fonts.googleapis.com/css2?family=Mulish:ital,wght@0,400;0,700;0,800;1,400&display=swap">
<style>
  :root {
    --bg: #d2d3d5;
    --red: #e0242f;
    --red-light: #e8614f;
    --red-deep: #d71f2b;
    --ink: #3f3f41;
    --ink-soft: #444446;
    --paper: #ffffff;
    --blush: #fcedee;
  }
  * { margin: 0; padding: 0; box-sizing: border-box; }
  html, body { width: 900px; height: 1200px; overflow: hidden; }
  body {
    background: var(--bg);
    font-family: "Mulish", sans-serif;
    position: relative;
  }
  .card {
    position: absolute;
    width: 655px;
    height: 375px;
    overflow: hidden;
  }
  .card-front { left: 124px; top: 190px; }
  .card-back { left: 123px; top: 622px; width: 656px; height: 376px; background: var(--paper); }

  .front-field {
    position: absolute; inset: 0;
    background: linear-gradient(90deg, var(--red-deep) 0%, var(--red) 50%, var(--red-light) 100%);
  }
  .front-mark {
    position: absolute;
    left: 50%; top: 50%;
    transform: translate(-50%, -50%);
    color: var(--paper);
    font-weight: 800;
    font-size: 30px;
    letter-spacing: 2px;
  }

  .back-accent {
    position: absolute;
    left: 472px; top: 0;
    width: 186px; height: 186px;
    border-radius: 50%;
    background: var(--blush);
  }
  .brand {
    position: absolute;
    left: 38px; top: 39px;
    display: flex; align-items: center;
  }
  .brand-square {
    width: 70px; height: 70px;
    background: var(--ink);
    margin-right: 14px;
  }
  .brand-name {
    font-weight: 800;
    font-size: 60px;
    line-height: 1;
    color: var(--ink);
    letter-spacing: 7px;
  }
  .brand-tagline {
    position: absolute;
    left: 122px; top: 97px;
    font-style: italic;
    font-size: 12px;
    letter-spacing: 1.4px;
    color: var(--ink-soft);
  }
  .person { position: absolute; left: 38px; top: 160px; }
  .person-name {
    font-weight: 700;
    font-size: 35px;
    line-height: 1.1;
    color: var(--red);
  }
  .person-role { font-size: 18px; color: var(--ink-soft); margin-top: 0; }
  .divider {
    position: absolute;
    left: 38px; top: 228px;
    width: 579px; height: 1.5px;
    background: var(--red);
  }
  .contacts {
    position: absolute;
    left: 38px; top: 236px;
    list-style: none;
  }
  .contacts li {
    display: flex; align-items: center;
    height: 27px;
    font-size: 18.5px;
    letter-spacing: 0.6px;
    color: var(--ink-soft);
  }
  .contacts li.phone { letter-spacing: 4px; }
  .contacts svg { width: 15px; height: 15px; margin-right: 8px; flex: none; }
  .address {
    position: absolute;
    right: 38px; top: 290px;
    text-align: right;
    font-size: 18.5px;
    letter-spacing: 0.6px;
    line-height: 27px;
    font-style: normal;
    color: var(--ink-soft);
  }
</style>
</head>
<body>

<section class="card card-front">
  <div class="front-field" role="img" aria-label="Embossed repeating brand-mark pattern on red"></div>
  <div class="front-mark">Velmo</div>
</section>

<section class="card card-back">
  <div class="back-accent" role="img" aria-label="Faint brand-mark decoration"></div>
  <div class="brand">
    <div class="brand-square"></div>
    <div class="brand-name">VELMO</div>
  </div>
  <div class="brand-tagline">A BOLD TAKE ON 3PL</div>

  <div class="person">
    <div class="person-name">Owen Trask</div>
    <div class="person-role">President</div>
  </div>
  <div class="divider"></div>

  <ul class="contacts">
    <li class="phone">
      <svg viewBox="0 0 24 24"><path fill="#e0242f" d="M6.6 10.8a15 15 0 0 0 6.6 6.6l2.2-2.2c.3-.3.7-.4 1-.2 1.1.4 2.3.6 3.6.6.6 0 1 .4 1 1V20c0 .6-.4 1-1 1A17 17 0 0 1 3 4c0-.6.4-1 1-1h3.5c.6 0 1 .4 1 1 0 1.3.2 2.5.6 3.6.1.3 0 .7-.2 1z"/></svg>
      +555-204-3186
    </li>
    <li class="phone">
      <svg viewBox="0 0 24 24"><rect x="6" y="2" width="12" height="20" rx="2" fill="none" stroke="#e0242f" stroke-width="2.4"/><circle cx="12" cy="18" r="1.3" fill="#e0242f"/></svg>
      +555-730-9142
    </li>
    <li>
      <svg viewBox="0 0 24 24"><rect x="2" y="5" width="20" height="14" fill="#e0242f"/><path d="M2 5l10 8 10-8" fill="none" stroke="#fff" stroke-width="1.8"/></svg>
      OTrask@velmo-llc.com
    </li>
    <li>
      <svg viewBox="0 0 24 24"><g fill="none" stroke="#e0242f" stroke-width="2"><circle cx="12" cy="12" r="9.5"/><ellipse cx="12" cy="12" rx="4" ry="9.5"/><path d="M2.5 12h19M4 7h16M4 17h16"/></g></svg>
      www.Velmo-LLC.com
    </li>
  </ul>

  <address class="address">
    1845 N. 250 East<br>
    Ashford, IN, 46019
  </address>
</section>

</body>
</html>
```